IT Business Card --- Quorvatek
Business card information technology
Professional
Mira Dunst
Senior System Consultant
47 Fernbrook Cres
Brackenford, L3K2P9
Westmere, Calderland.
mira.dunst@quorvatekhub.com
www.quorvatekhub.com
PNXA #4183 Voice, R&S
This is my logo in AI format

```html
<!DOCTYPE html>
<html lang="en">
<head>
<meta charset="UTF-8">
<title>Quorvatek Business Card</title>
<link href="https://fonts.googleapis.com/css2?family=Arimo:wght@400;700&display=swap" rel="stylesheet">
<style>
  :root {
    --bg-light: #f2f2f2;
    --bg-dark: #c9c9c9;
    --red: #d41f26;
    --red-dark: #9e1117;
    --red-light: #e8413f;
    --white: #ffffff;
    --paper: #f7f7f7;
    --grey-text: #6a6a6a;
    --ink: #3a3a3a;
  }
  * { margin: 0; padding: 0; box-sizing: border-box; }
  html, body { width: 1200px; height: 1016px; overflow: hidden; }
  body {
    background: radial-gradient(ellipse at center, var(--bg-light) 0%, var(--bg-dark) 100%);
    font-family: "Arimo", Arial, sans-serif;
    position: relative;
  }
  .card {
    position: absolute;
    left: 250px;
    width: 700px;
    height: 400px;
    border-radius: 22px;
    overflow: hidden;
    box-shadow: 0 10px 30px rgba(0,0,0,0.25);
  }
  .card-front { top: 70px; background: var(--paper); }
  .card-back {
    top: 540px;
    background: linear-gradient(160deg, var(--red-light) 0%, var(--red) 45%, var(--red-dark) 100%);
  }
  .swoosh { position: absolute; inset: 0; width: 100%; height: 100%; }
  .brand {
    position: absolute;
    display: flex;
    align-items: center;
    gap: 14px;
    font-weight: 700;
  }
  .card-front .brand { left: 46px; top: 66px; color: var(--ink); font-size: 42px; }
  .card-front .brand-mark { width: 36px; height: 36px; background: var(--ink); }
  .card-back .brand {
    left: 0; right: 0; top: 156px;
    justify-content: center;
    color: var(--white); font-size: 52px;
  }
  .card-back .brand-mark { width: 44px; height: 44px; background: var(--white); }
  .contact {
    position: absolute;
    right: 40px;
    top: 30px;
    text-align: right;
    color: var(--grey-text);
    font-size: 14px;
    line-height: 1.5;
  }
  .holder {
    position: absolute;
    left: 46px;
    top: 238px;
    color: var(--white);
  }
  .holder-name { font-size: 30px; font-weight: 700; }
  .holder-title { font-size: 15px; margin-top: 4px; }
  .holder-cert {
    position: absolute;
    left: 46px;
    bottom: 34px;
    color: var(--white);
    font-size: 17px;
    font-weight: 700;
    letter-spacing: 0.5px;
  }
  .web-pill {
    position: absolute;
    right: 0;
    bottom: 34px;
    width: 300px;
    height: 44px;
    background: var(--paper);
    border-radius: 22px 0 0 22px;
    display: flex;
    align-items: center;
    justify-content: center;
    color: var(--grey-text);
    font-size: 15px;
  }
</style>
</head>
<body>
  <section class="card card-front">
    <svg class="swoosh" viewBox="0 0 700 400" preserveAspectRatio="none" aria-hidden="true">
      <path d="M0 255 C180 200 420 172 700 188 L700 194 C430 180 190 212 0 280 Z" fill="#bdbdbd"/>
      <path d="M0 215 C200 178 430 175 700 205 L700 400 L0 400 Z" fill="var(--red)"/>
      <path d="M0 215 C200 178 430 175 700 205 L700 220 C430 193 200 198 0 237 Z" fill="var(--red-light)"/>
    </svg>
    <div class="brand"><span class="brand-mark"></span><span class="brand-name">Quorvatek</span></div>
    <div class="contact">
      <p>T: 1 (555) 204 7731</p>
      <p>mira.dunst@quorvatekhub.com</p>
      <p>www.quorvatekhub.com</p>
      <p>47 Fernbrook Cres</p>
      <p>Brackenford, L3K2P9</p>
      <p>Westmere, Calderland.</p>
    </div>
    <div class="holder">
      <p class="holder-name">Mira Dunst</p>
      <p class="holder-title">Senior System Consultant</p>
    </div>
    <p class="holder-cert">PNXA #4183 Voice, R&amp;S</p>
  </section>

  <section class="card card-back">
    <div class="brand"><span class="brand-mark"></span><span class="brand-name">Quorvatek</span></div>
    <div class="web-pill">www.quorvatekhub.com</div>
  </section>
</body>
</html>
```